DOOR HANGER BACK
When you describe our services label like this
Interior | Exterior
Residential | Commercial
Wall Covering | Epoxy Flooring | Lacquer Packages
however you want to do it but some thing like that
Email Address is briarfieldpainting@maildrop.example i don't know if you want to add the to the front or back of door hanger
Website is briarfieldpainting.example
i want to exterior picture on the front of the door hanger and the interior one on the back.
DOOR HANGER FRONT
i want 4 check marks Licensed Bonded Insured Proffessional get rid of with low rates .
i was thinking of adding a saying goes like this “Better Quality, Best Prices, Guaranteed” so you could put that on the front of your marketing stuff help fill any space.
could you use the magnify glass with the roller on the front of the door hanger. or would that not work??
FLYER BACK
the about us just needs the proper spacing in the beginning. [tab] all other small changes
FLYER FRONT
change picture fix all the other stuff we talked about and i was wondering what it would look like with our phone number next to FREE ESTIMATES and maybe fill its space with a contact us and our email.
POST CARD FRONT
same things mentioned
POST CARD BACK
YARD SIGN
BIZ CARD FRONT
name Dana Prescott title Project Manager
BIZ CARD BACK
quick changes
Vinyl banner
change picture
thanks so much jo for your help im so excited to see your changes
Briarfield Hollow Painting is a Full service painting company, Qualified in all types of painting materials and application processes. We are the painting experts! Although we are a fairly new company we have been in the painting industry for quite sometime. Our staff has over 50 years combined experience. Since we are a newly established company here in oregon we will be offer rates much lower then are competitors and our quality and workmanship is unsurpassed. Guaranteed! Let us come paint your home so you can see personally what sets us apart from all the others.
Testimonials
I want to send a brief letter to you expressing my appreciation and praise for Briarfield Hollow Painting. Your company has transformed my home from an eye soar in the neighborhood, to the most beautiful home on the block! My neighbors are asking for you information thank you so much!
~Lori Brenton~
Your customer service was second to none. I cant believe how attentive you guys are. What ever I needed whenever you guys always took care of it. It is amazing how hard your guys work and how quickly they painted my home. They did an outstanding job!
~Mark Ellison~
What sets us apart
* Professionalism and service- Top notch
* Customer services is our priority
* Quality workmanship - no one else comes close
* Fully Licensed Bonded Insured in Oregon
* Over 50 years experience of our combined staff
* Expert in all types of residential Painting
* 2 year Limited workmanship warranty
* Fully Supervised Job sites at all times.
* Incentives such as discounts, gutter and roof cleaning
best regards
dana prescott
Briarfield hollow painting is a newly established company but withh over 35 years experience between all of us.
address is 18472 SE Fobbler Rd. Gresham,OR 97099
http://orders.brandtilehub.example/contests/roofing-company-canvassing-and-sales-material

```html
<!DOCTYPE html>
<html lang="en">
<head>
<meta charset="utf-8">
<title>Briarfield Hollow Painting – Marketing Set</title>
<link href="https://fonts.googleapis.com/css2?family=Roboto:wght@400;700;900&family=Roboto+Condensed:ital,wght@0,700;1,700&display=swap" rel="stylesheet">
<style>
:root{
  --board:#1b1b1d;
  --board-label:#9a9a9a;
  --orange:#f58220;
  --orange-deep:#d9581a;
  --orange-soft:#ffb347;
  --navy:#1d3c78;
  --sky-top:#5d93d6;
  --sky-bottom:#cfe2f5;
  --house:#d8c7a8;
  --white:#ffffff;
  --ink:#222222;
  --sticky:#ffd23a;
}
*{box-sizing:border-box;margin:0;padding:0}
html,body{width:1200px;height:1021px;overflow:hidden;background:var(--board)}
body{position:relative;font-family:"Roboto",Arial,sans-serif;color:var(--ink)}
.piece{position:absolute;overflow:hidden}
.label{position:absolute;color:var(--board-label);font-size:10px;letter-spacing:.5px;text-transform:uppercase;font-family:"Roboto",Arial,sans-serif}
.photo{background:linear-gradient(180deg,var(--sky-top),var(--sky-bottom) 55%,var(--house))}
.photo-interior{background:linear-gradient(160deg,#f1e6d2,#c9a77c)}
.tool{background:radial-gradient(circle at 40% 40%,#f0f0f0,#9aa3ad 60%,#5b6670)}
.brand{display:flex;align-items:center;gap:5px;font-weight:700;color:var(--navy)}
.brand-mark{width:12px;height:12px;background:var(--orange);flex:none}
.free{font-family:"Roboto Condensed",Arial,sans-serif;font-weight:700;color:var(--white);line-height:.9}
.free b{display:block}
.call{font-family:"Roboto Condensed",Arial,sans-serif;font-weight:700;color:var(--white)}
.ticks{list-style:none}
.ticks li{display:flex;align-items:center;gap:4px;color:var(--white);font-weight:700;background:var(--navy);margin-bottom:3px;padding:2px 5px;border-radius:3px}
.ticks li::before{content:"✔";color:var(--orange-soft)}
.services h4{color:var(--orange);font-weight:900;text-transform:uppercase}
.orange-band{background:linear-gradient(180deg,var(--orange),var(--orange-deep))}

/* door hangers */
.hanger{width:165px;height:440px;border-radius:70px 70px 10px 10px}
.hanger-hole{position:absolute;left:50%;top:26px;width:70px;height:70px;margin-left:-35px;border-radius:50%;background:var(--board)}
.hanger-slot{position:absolute;left:50%;top:70px;width:12px;height:48px;margin-left:-6px;background:var(--board)}
.hanger-back{left:40px;top:40px;background:var(--orange)}
.hanger-back .photo-interior{position:absolute;left:0;top:0;width:100%;height:210px}
.hanger-back .panel{position:absolute;left:10px;right:10px;top:220px;bottom:10px;background:var(--white);border-radius:6px;padding:8px;font-size:8px}
.hanger-back .services h4{font-size:10px;margin-bottom:3px}
.hanger-back .services p{font-size:8px;line-height:1.35}
.hanger-back .call{color:var(--orange-deep);font-size:17px;margin:8px 0 6px}
.hanger-back .brand{font-size:9px;margin-bottom:6px}
.hanger-back .contact{font-size:6.5px;line-height:1.4;color:#444}
.hanger-front{left:220px;top:40px;background:var(--orange)}
.hanger-front .photo{position:absolute;left:0;top:0;width:100%;height:235px}
.hanger-front .free{position:absolute;left:12px;top:245px;font-size:44px}
.hanger-front .free b:last-child{font-size:26px}
.hanger-front .call{position:absolute;left:12px;top:345px;font-size:17px}
.hanger-front .slogan{position:absolute;left:12px;right:10px;top:372px;font-size:8px;color:var(--white);font-weight:700}
.hanger-front .brand{position:absolute;left:12px;bottom:14px;background:var(--white);padding:4px 6px;border-radius:4px;font-size:8px}

/* flyers */
.flyer{width:265px;height:340px;background:var(--white)}
.flyer-back{left:410px;top:30px;padding:12px;font-size:6px;line-height:1.35}
.flyer-back .cols{display:flex;gap:10px}
.flyer-back .col{flex:1}
.flyer-back h3{color:var(--orange-deep);font-size:10px;margin-bottom:3px}
.flyer-back p{text-indent:10px;margin-bottom:4px}
.flyer-back .services{background:var(--white);border:1px solid #eee;padding:4px}
.flyer-back .services h4{font-size:9px}
.flyer-back .testimonial{background:var(--sticky);padding:5px;transform:rotate(-3deg);margin:6px 0;box-shadow:1px 2px 3px rgba(0,0,0,.25)}
.flyer-back ul{padding-left:10px}
.flyer-back .foot{position:absolute;left:0;right:0;bottom:0;height:22px;background:var(--orange);color:var(--white);font-size:7px;display:flex;align-items:center;justify-content:center;font-weight:700}
.flyer-back .photo-interior{height:70px;margin-top:4px}
.flyer-front{left:760px;top:30px}
.flyer-front .photo{position:absolute;inset:0 0 120px 0}
.flyer-front .tool{position:absolute;right:12px;top:30px;width:90px;height:90px;border-radius:50%}
.flyer-front .ticks{position:absolute;left:12px;top:40px;font-size:9px}
.flyer-front .orange-band{position:absolute;left:0;right:0;bottom:0;height:135px;padding:10px 12px}
.flyer-front .free{font-size:46px;transform:rotate(-6deg);transform-origin:left}
.flyer-front .free b:last-child{font-size:28px}
.flyer-front .call{font-size:18px;margin-top:8px}
.flyer-front .web{font-size:7px;color:var(--white);margin-top:3px}

/* yard sign */
.yard-sign{left:40px;top:600px;width:340px;height:175px;background:var(--white);border:5px solid var(--orange)}
.yard-sign .brand{position:absolute;left:14px;top:12px;font-size:11px}
.yard-sign .free{position:absolute;left:14px;top:38px;color:var(--orange-deep);font-size:52px}
.yard-sign .free b:last-child{font-size:30px}
.yard-sign .call{position:absolute;left:0;right:0;bottom:0;height:34px;background:var(--orange);font-size:22px;display:flex;align-items:center;padding-left:14px}
.yard-sign .photo{position:absolute;right:10px;top:12px;width:110px;height:110px}
.stake{position:absolute;top:775px;width:5px;height:45px;background:#8a8a8a}

/* postcards */
.postcard{width:370px;height:250px}
.postcard-back{left:400px;top:400px;background:var(--white);padding:10px;font-size:5.6px;line-height:1.35}
.postcard-back .left{position:absolute;left:10px;top:10px;width:190px}
.postcard-back .right{position:absolute;right:10px;top:10px;width:150px;bottom:40px;border-left:1px solid #ccc;padding-left:8px}
.postcard-back h3{color:var(--orange-deep);font-size:8px;margin-bottom:2px}
.postcard-back p{text-indent:8px;margin-bottom:3px}
.postcard-back .testimonial{background:var(--sticky);padding:4px;margin:4px 0;transform:rotate(-2deg)}
.postcard-back .stamp{position:absolute;right:0;top:0;width:30px;height:36px;border:1px dashed #999}
.postcard-back .addr-lines{position:absolute;left:8px;right:8px;top:90px}
.postcard-back .addr-lines span{display:block;border-bottom:1px solid #bbb;height:14px}
.postcard-back .foot{position:absolute;left:0;right:0;bottom:0;height:20px;background:var(--orange);color:var(--white);font-weight:700;font-size:7px;display:flex;align-items:center;justify-content:center}
.postcard-front{left:820px;top:400px;background:var(--orange)}
.postcard-front .photo{position:absolute;right:0;top:0;width:200px;height:250px}
.postcard-front .tool{position:absolute;right:20px;top:20px;width:80px;height:80px;border-radius:50%}
.postcard-front .brand{position:absolute;left:12px;top:12px;background:var(--white);padding:4px 6px;border-radius:4px;font-size:9px}
.postcard-front .ticks{position:absolute;left:12px;top:40px;font-size:8.5px}
.postcard-front .free{position:absolute;left:12px;top:128px;font-size:46px;transform:rotate(-6deg);transform-origin:left}
.postcard-front .free b:last-child{font-size:28px}
.postcard-front .call{position:absolute;left:12px;bottom:12px;font-size:20px}

/* business cards */
.biz{top:840px;width:270px;height:125px}
.biz-back{left:40px;background:var(--orange);padding:14px}
.biz-back .brand{color:var(--white);font-size:13px}
.biz-back .brand-mark{background:var(--white)}
.biz-back .services{position:absolute;left:14px;bottom:12px;font-size:6.5px;color:var(--white);line-height:1.4}
.biz-front{left:325px;background:var(--white)}
.biz-front .orange-band{position:absolute;left:0;top:0;bottom:0;width:100px;display:flex;align-items:center;justify-content:center}
.biz-front .orange-band .brand{color:var(--white);font-size:9px;flex-direction:column;text-align:center;padding:6px}
.biz-front .orange-band .brand-mark{background:var(--white)}
.biz-front .info{position:absolute;left:112px;top:16px;right:10px;font-size:7px;line-height:1.45}
.biz-front .info strong{display:block;font-size:11px;color:var(--orange-deep)}
.biz-front .info em{display:block;font-style:normal;color:#666;margin-bottom:6px}

/* banner */
.banner{left:640px;top:740px;width:390px;height:230px;background:var(--navy)}
.banner .photo{position:absolute;left:0;top:0;width:160px;height:200px}
.banner .free{position:absolute;left:172px;top:14px;font-size:50px;color:var(--orange)}
.banner .free b:last-child{font-size:30px;color:var(--white)}
.banner .call{position:absolute;left:172px;top:118px;font-size:19px}
.banner .services{position:absolute;left:172px;top:146px;font-size:6.5px;color:var(--white);line-height:1.4}
.banner .services h4{font-size:8px}
.banner .foot{position:absolute;left:0;right:0;bottom:0;height:30px;display:flex;align-items:center;justify-content:space-around;font-size:8px;font-weight:700;color:var(--white)}
</style>
</head>
<body>

<div class="label" style="left:40px;top:16px">Door hanger</div>
<div class="label" style="left:410px;top:12px">Flyer</div>

<!-- Door hanger back -->
<section class="piece hanger hanger-back">
  <div class="photo-interior" role="img" aria-label="Photo of a freshly painted interior room"></div>
  <div class="hanger-hole"></div><div class="hanger-slot"></div>
  <div class="panel">
    <div class="services">
      <h4>Our services:</h4>
      <p>Interior | Exterior<br>Residential | Commercial<br>Wall Covering | Epoxy Flooring<br>Lacquer Packages</p>
    </div>
    <div class="call">Call us 5035550142</div>
    <div class="brand"><span class="brand-mark"></span>Briarfield Hollow Painting</div>
    <p class="contact">briarfieldpainting@maildrop.example<br>briarfieldpainting.example<br>18472 SE Fobbler Rd. Gresham,OR 97099</p>
  </div>
</section>
<div class="label" style="left:105px;top:490px">Back</div>

<!-- Door hanger front -->
<section class="piece hanger hanger-front">
  <div class="photo" role="img" aria-label="Photo of a painted house exterior with a magnifying glass and paint roller"></div>
  <div class="hanger-hole"></div><div class="hanger-slot"></div>
  <div class="free"><b>Free</b><b>estimates</b></div>
  <div class="call">Call us 5035550142</div>
  <p class="slogan">Better Quality, Best Prices, Guaranteed</p>
  <div class="brand"><span class="brand-mark"></span>Briarfield Hollow Painting</div>
</section>
<div class="label" style="left:285px;top:490px">Front</div>

<!-- Flyer back -->
<section class="piece flyer flyer-back">
  <div class="cols">
    <div class="col">
      <h3>About Us</h3>
      <p>Briarfield Hollow Painting is a Full service painting company, Qualified in all types of painting materials and application processes. We are the painting experts! Our staff has over 50 years combined experience. Let us come paint your home so you can see personally what sets us apart.</p>
      <h3>What sets us apart</h3>
      <ul>
        <li>Professionalism and service- Top notch</li>
        <li>Customer services is our priority</li>
        <li>Quality workmanship</li>
        <li>Fully Licensed Bonded Insured in Oregon</li>
        <li>2 year Limited workmanship warranty</li>
        <li>Fully Supervised Job sites at all times</li>
      </ul>
      <div class="photo-interior" role="img" aria-label="Photo of a painted interior"></div>
    </div>
    <div class="col">
      <div class="services">
        <h4>Our services:</h4>
        <p>Interior | Exterior<br>Residential | Commercial<br>Wall Covering | Epoxy Flooring<br>Lacquer Packages</p>
      </div>
      <h3 style="margin-top:6px">Testimonials</h3>
      <div class="testimonial">Your company has transformed my home from an eye sore in the neighborhood, to the most beautiful home on the block! ~Lori Brenton~</div>
      <div class="testimonial">Your customer service was second to none. They did an outstanding job! ~Mark Ellison~</div>
      <p>18472 SE Fobbler Rd. Gresham,OR 97099</p>
    </div>
  </div>
  <div class="foot">briarfieldpainting.example</div>
</section>
<div class="label" style="left:510px;top:378px">Flyer back</div>

<!-- Flyer front -->
<section class="piece flyer flyer-front">
  <div class="photo" role="img" aria-label="Photo of a freshly painted house exterior"></div>
  <div class="tool" role="img" aria-label="Illustration of a magnifying glass with a paint roller"></div>
  <ul class="ticks"><li>Licensed</li><li>Bonded</li><li>Insured</li><li>Professional</li></ul>
  <div class="orange-band">
    <div class="free"><b>Free</b><b>estimates</b></div>
    <div class="call">Call us 5035550142</div>
    <div class="web">briarfieldpainting.example</div>
  </div>
</section>
<div class="label" style="left:860px;top:378px">Flyer front</div>

<!-- Yard sign -->
<div class="label" style="left:40px;top:582px">Yard signs</div>
<section class="piece yard-sign">
  <div class="brand"><span class="brand-mark"></span>Briarfield Hollow Painting</div>
  <div class="photo" role="img" aria-label="Photo of a painted house exterior"></div>
  <div class="free"><b>Free</b><b>estimates</b></div>
  <div class="call">Call us 5035550142</div>
</section>
<div class="stake" style="left:100px"></div>
<div class="stake" style="left:315px"></div>

<!-- Postcard back -->
<section class="piece postcard postcard-back">
  <div class="left">
    <h3>About Us</h3>
    <p>Briarfield Hollow Painting is a Full service painting company, Qualified in all types of painting materials and application processes. Our staff has over 50 years combined experience.</p>
    <div class="testimonial">Your company has transformed my home! ~Lori Brenton~</div>
    <h3>What sets us apart</h3>
    <p>Quality workmanship, fully Licensed Bonded Insured in Oregon, 2 year Limited workmanship warranty.</p>
  </div>
  <div class="right">
    <h3>Our services:</h3>
    <p>Interior | Exterior · Residential | Commercial · Wall Covering | Epoxy Flooring · Lacquer Packages</p>
    <div class="stamp"></div>
    <div class="addr-lines"><span></span><span></span><span></span></div>
  </div>
  <div class="foot">briarfieldpainting.example</div>
</section>
<div class="label" style="left:540px;top:660px">Postcard back</div>

<!-- Postcard front -->
<section class="piece postcard postcard-front">
  <div class="photo" role="img" aria-label="Photo of a freshly painted house exterior"></div>
  <div class="tool" role="img" aria-label="Illustration of a magnifying glass with a paint roller"></div>
  <div class="brand"><span class="brand-mark"></span>Briarfield Hollow Painting</div>
  <ul class="ticks"><li>Licensed</li><li>Bonded</li><li>Insured</li><li>Professional</li></ul>
  <div class="free"><b>Free</b><b>estimates</b></div>
  <div class="call">Call us 5035550142</div>
</section>
<div class="label" style="left:1080px;top:660px">Postcard front</div>

<!-- Business card back -->
<section class="piece biz biz-back">
  <div class="brand"><span class="brand-mark"></span>Briarfield Hollow Painting</div>
  <p class="services">Interior | Exterior<br>Residential | Commercial<br>Wall Covering | Epoxy Flooring | Lacquer Packages</p>
</section>
<div class="label" style="left:120px;top:975px">Business card – back</div>

<!-- Business card front -->
<section class="piece biz biz-front">
  <div class="orange-band"><div class="brand"><span class="brand-mark"></span>Briarfield Hollow Painting</div></div>
  <div class="info">
    <strong>Dana Prescott</strong>
    <em>Project Manager</em>
    Call 5035550142<br>
    briarfieldpainting@maildrop.example<br>
    briarfieldpainting.example<br>
    18472 SE Fobbler Rd.<br>Gresham,OR 97099
  </div>
</section>
<div class="label" style="left:400px;top:975px">Business card – front</div>

<!-- Vinyl banner -->
<section class="piece banner">
  <div class="photo" role="img" aria-label="Photo of a freshly painted house exterior"></div>
  <div class="free"><b>Free</b><b>estimates</b></div>
  <div class="call">Call us 5035550142</div>
  <div class="services">
    <h4>Our services:</h4>
    <p>Interior | Exterior | Residential | Commercial<br>Wall Covering | Epoxy Flooring | Lacquer Packages</p>
  </div>
  <div class="foot orange-band"><span>briarfieldpainting@maildrop.example</span><span>briarfieldpainting.example</span></div>
</section>
<div class="label" style="left:1045px;top:900px">Vinyl banner</div>

</body>
</html>
```